Lorenz und Mathilde Poster

We need a poser for the production of the Brandtners opera - Lorenz und Mathilde.

Target Market(s)

opera, music goers

Colors

Designer to choose colors to be used in the design.

Requirements
Must have
• Dates and names, logos, people, space for sponsors, contact info
• Harrowgate Lyric Opera
• Pellham Cantabile Chamber Orchestra
• Lorenz und Mathilde
• by Konrad Brandtner
• Mavis Dunlow - Lorenz
• Polly Kent - Mathilde
• Oksana Beletskaya - Ottilie
• Ferrol Haupner - Gaspard
• Glen Oosterhout - König Aldric
• Barry Whitcombe - Renwick
• Peter Vrodosek - shepherd / young Sailor
• Lucas Penhollow - Director, conductor
• Performances:
• Friday, November 8th 7:00pm at Cobbleford Hall in New Britain
• Saturday, November 16th 7:00pm at Ruelle Beaumarch Performing Arts Center in Middletown
• Sunday, November 17th 2:00pm at the Pemberly Gallerium in Hartford
• Saturday November 30th 7:00pm at the Lintel Arts Center in New London
• (860) 555-PCCO (7226)
• info@pellhamcantabile.org
• www.harrowgatelyric.org
• www.pellhamcantabile.org
Nice to have
• Modern design touch

```html
<!DOCTYPE html>
<html lang="en">
<head>
<meta charset="utf-8">
<title>Lorenz und Mathilde Poster</title>
<link rel="stylesheet" href="https://fonts.googleapis.com/css2?family=Forum&family=Rye&display=swap">
<style>
  :root {
    --page: #ffffff;
    --poster: #000000;
    --ink: #ffffff;
    --copper: #a8735c;
    --wine: #9b1c1c;
    --rule: #ffffff;
  }
  * { margin: 0; padding: 0; box-sizing: border-box; }
  html, body { width: 1200px; height: 1200px; overflow: hidden; background: var(--page); }
  body { position: relative; font-family: "Forum", serif; color: var(--ink); text-transform: uppercase; }
  .poster { position: absolute; left: 252px; top: 116px; width: 696px; height: 968px; background: var(--poster); }
  .abs { position: absolute; white-space: nowrap; }

  .series { left: 0; width: 100%; top: 11px; text-align: center; font-size: 26px; letter-spacing: 0.3px; }
  .series-rule { top: 28px; height: 1.5px; width: 108px; background: var(--rule); }

  .presenters { left: 0; width: 100%; top: 71px; text-align: center; font-size: 16px; line-height: 18px; color: var(--copper); }

  .title-art { position: absolute; left: 0; top: 0; width: 696px; height: 560px; }
  .title-word { font-family: "Rye", serif; }

  .composer { left: 0; width: 100%; padding-left: 120px; text-align: center; top: 364px; font-size: 34px; letter-spacing: -0.5px;
    background: linear-gradient(90deg, transparent 0%, transparent 28%, #b07a2a 30%, #8a8a86 50%, #6f6d6a 80%);
    -webkit-background-clip: text; background-clip: text; color: transparent; }

  .perf-heading { left: 26px; top: 452px; font-size: 17px;
    background: linear-gradient(90deg, #fff 0%, #fff 12%, #7a5a50 30%, #7a5a50 100%);
    -webkit-background-clip: text; background-clip: text; color: transparent; }
  .show { left: 26px; width: 320px; }
  .show-date { font-size: 18px; line-height: 19px; }
  .show-place { font-size: 13px; line-height: 15.5px; white-space: normal; }

  .left-rule { left: 26px; top: 747px; width: 315px; height: 2px; background: var(--rule); }
  .contact-heading { left: 0; width: 346px; top: 775px; text-align: center; font-size: 14px; }
  .contact-lines { left: 79px; top: 803px; font-size: 15px; line-height: 16.8px; }

  .partner { top: 911px; height: 39px; background: #fff; color: var(--wine); display: flex; align-items: center; justify-content: center; font-size: 11px; line-height: 11px; text-align: center; }
  .partner-opera { left: 32px; width: 92px; }
  .partner-orch { left: 130px; width: 196px; font-size: 17px; }

  .divider { left: 357px; top: 426px; width: 2px; height: 501px; background: var(--rule); }

  .cast { left: 375px; top: 422px; }
  .cast-row { display: flex; align-items: center; height: 54.5px; }
  .headshot { width: 49px; height: 49px; border: 1px solid #d9d9d9; padding: 2px; background: #000; }
  .headshot span { display: block; width: 100%; height: 100%; }
  .cast-name { margin-left: 4px; font-size: 10.5px; }

  .sponsor-label { left: 388px; top: 866px; font-size: 11px; }
  .sponsor-box { left: 385px; top: 884px; width: 297px; height: 71px; border: 1px solid #fff; }
</style>
</head>
<body>
<main class="poster">
  <div class="abs series-rule" style="left:70px"></div>
  <div class="abs series">The Brandtners Opera</div>
  <div class="abs series-rule" style="left:518px"></div>

  <div class="abs presenters">Harrowgate Lyric Opera<br>Pellham Cantabile Chamber Orchestra</div>

  <svg class="title-art" viewBox="0 0 696 560" aria-label="Lorenz und Mathilde">
    <defs>
      <linearGradient id="letterTone" x1="0" y1="0" x2="1" y2="1">
        <stop offset="0" stop-color="#9a7d78"/>
        <stop offset="0.5" stop-color="#7f6f72"/>
        <stop offset="1" stop-color="#5d5963"/>
      </linearGradient>
    </defs>
    <rect role="img" aria-label="Painted scene of the lovers, red tones" x="173" y="112" width="202" height="200" fill="#b42828" opacity="0.85"/>
    <rect role="img" aria-label="Painted scene, dark umber tones" x="76" y="266" width="153" height="158" fill="#3a2410" opacity="0.8"/>
    <rect role="img" aria-label="Painted detail, yellow-green tones" x="366" y="281" width="78" height="81" fill="#b9c933" opacity="0.8"/>

    <g class="title-word" stroke="#000" stroke-width="2">
      <text x="51" y="232" font-size="150" textLength="579" lengthAdjust="spacingAndGlyphs" fill="#2a2222">LORENZ</text>
      <text x="45" y="226" font-size="150" textLength="579" lengthAdjust="spacingAndGlyphs" fill="url(#letterTone)" fill-opacity="0.85">LORENZ</text>
      <text x="51" y="269" font-size="44" textLength="84" lengthAdjust="spacingAndGlyphs" fill="#6d6468">UND</text>
      <text x="150" y="353" font-size="150" textLength="470" lengthAdjust="spacingAndGlyphs" fill="#2a2222">MATHILDE</text>
      <text x="144" y="347" font-size="150" textLength="470" lengthAdjust="spacingAndGlyphs" fill="url(#letterTone)" fill-opacity="0.85">MATHILDE</text>
    </g>
    <rect x="144" y="355" width="472" height="5" rx="2.5" fill="#8a7f78"/>
  </svg>

  <div class="abs composer">By Konrad Brandtner</div>

  <div class="abs perf-heading">Performances:</div>
  <div class="abs show" style="top:494px">
    <div class="show-date">Friday, November 8th 7:00pm</div>
    <div class="show-place">At Cobbleford Hall in New Britain</div>
  </div>
  <div class="abs show" style="top:549px">
    <div class="show-date">Saturday, November 16th 7:00pm</div>
    <div class="show-place">At Ruelle Beaumarch Performing Arts Center in Middletown</div>
  </div>
  <div class="abs show" style="top:619px">
    <div class="show-date">Sunday, November 17th 2:00pm</div>
    <div class="show-place">At the Pemberly Gallerium in Hartford</div>
  </div>
  <div class="abs show" style="top:673px">
    <div class="show-date">Saturday November 30th 7:00pm</div>
    <div class="show-place">At the Lintel Arts Center in New London<br>(860) 555-PCCO (7226)</div>
  </div>

  <div class="abs left-rule"></div>
  <div class="abs contact-heading">Contact info :</div>
  <div class="abs contact-lines">info@pellhamcantabile.org<br>www.harrowgatelyric.org<br>www.pellhamcantabile.org</div>

  <div class="abs partner partner-opera">Harrowgate<br>Lyric Opera</div>
  <div class="abs partner partner-orch">Pellham Cantabile</div>

  <div class="abs divider"></div>

  <div class="abs cast">
    <div class="cast-row"><div class="headshot"><span role="img" aria-label="Portrait of Mavis Dunlow" style="background:linear-gradient(#9a9a9a,#2b2b2b)"></span></div><div class="cast-name">Mavis Dunlow - Lorenz</div></div>
    <div class="cast-row"><div class="headshot"><span role="img" aria-label="Portrait of Polly Kent" style="background:linear-gradient(#e9e6e4,#6b3b33)"></span></div><div class="cast-name">Polly Kent - Mathilde</div></div>
    <div class="cast-row"><div class="headshot"><span role="img" aria-label="Portrait of Oksana Beletskaya" style="background:linear-gradient(#3a2620,#8a3a36)"></span></div><div class="cast-name">Oksana Beletskaya - Ottilie</div></div>
    <div class="cast-row"><div class="headshot"><span role="img" aria-label="Portrait of Ferrol Haupner" style="background:linear-gradient(#c98e6f,#6d3a2a)"></span></div><div class="cast-name">Ferrol Haupner - Gaspard</div></div>
    <div class="cast-row"><div class="headshot"><span role="img" aria-label="Portrait of Glen Oosterhout" style="background:linear-gradient(#5a5a5a,#c4906e)"></span></div><div class="cast-name">Glen Oosterhout - König Aldric</div></div>
    <div class="cast-row"><div class="headshot"><span role="img" aria-label="Portrait of Barry Whitcombe" style="background:linear-gradient(#6a6058,#2c3a4a)"></span></div><div class="cast-name">Barry Whitcombe - Renwick</div></div>
    <div class="cast-row"><div class="headshot"><span role="img" aria-label="Portrait of Peter Vrodosek" style="background:linear-gradient(#8a6a3a,#3a2818)"></span></div><div class="cast-name">Peter Vrodosek - Shepherd / Young Sailor</div></div>
    <div class="cast-row"><div class="headshot"><span role="img" aria-label="Portrait of Lucas Penhollow" style="background:linear-gradient(#1a1a1a,#d8d2cc)"></span></div><div class="cast-name">Lucas Penhollow - Director, conductor</div></div>
  </div>

  <div class="abs sponsor-label">Space for sponsors</div>
  <div class="abs sponsor-box"></div>
</main>
</body>
</html>
```